Vela Sorrin Design Project

Velá Sorrin is a new store in California that offers a large variety of premium, fresh olive oils and balsamic vinegars for tasting and purchase. These products will appeal to health conscious individuals of all ages and desired by those that consider themselves fit, healthy, and love their food. The stores will also carry high-end contemporary art from local artists to enhance the contemporary feel of the store and add to the ambiance / experience.

The logo (attached) may help with the design approach. See attached documents. I have also uploaded some pictures of art.

The main objective of this design exercise is to solicit ideas for overall design (look and feel, color, layout) and the menuing system.

The website design is not a trivial exercise as it needs to be simple, clean, crisp and contemporary, while being easy to navigate and to easily purchase products. When someone comes to our home page we want them to feel they have never been to a site like this and yet find it easy to get to the information they need. It can not be busy. The look and feel should be fitting with our logo and the type of contemporary art we carry.

The menu system will be extremely important. We don't want too many menu items (ideally 5 max) yet we have to make it intuitive to find products and information. We are interested in your ideas for naming these menu items based on your experience with other site. For example, should we have "Contact" as a main menu item or is there an intuitive way of putting contact info in another category...or somewhere completely different on the page? Another challenge, we don't want to use the generic term "products" but using "Balsamic Vinegars" and "Olive Oils" may be too long.

The products we will carry include
- olive oils (20- 30)
- balsamic vinegars (15-20)
- accessories for oils and vinegars such as bottles (40- 50)
- art (3 - 5 artists)
- possibly wine later (10-15)

Olive oils could be categorized in the following ways. We may need to pick one approach or figure out a way to let customers navigate the options based on their interests and taste?
- Alphabetically
- Their origin (region, Europe , South America)
- Olive type (Greek, Italian, etc.)
- Flavor (peppery, smooth, infused/flavored...)
- Top sellers
- and possibly other options we haven't considered yet.

Balsamic Vinegars will be categorized primarily by flavor.

Accessories should be found independently from other products but will also be sorted by appropriateness. Example, olive oil spouts under olive oils or balsamic bottle holders under balsamics.

Art is a little easier as there will be only a few artists under which we will display a small number of pieces of their work. They will be categorized by name.

In each scenario we will want the customer to easily navigate to the particular "product page" which will contain an image of the product and all the information they will need. Note, we source the products in bulk so all the bottles will look similar ...with our logo. We won't offer different shapes and sizes from different producers.

Each product page will have a summary of the product with "more information" available to the user. The "purchase now" should be intuitive. Available bottle sizes will be 220ml, 375 ml, 750ml

As noted above, we will want a display area for relevant accessories and other product recommendations based on other peoples purchases (or what we think is a good companion).

If there is more information that would help with the process let me know.
Updates

Reason: Hi Designers. Given the upcoming holiday in the US (where I live) I've decided to extend the deadline till November 30th. I will have access to email and Pixel Guild but my responses my be a little delayed and I just want to apologize for that in advance. Regards, Neil

Reason: Hi All. I just returned from a week of traveling and sent those of you who had submitted designs some feedback. I you did not receive any feedback please contact me. To give those of you some additional time to review my feedback and make edits I'm extending the project till the end of this weekend. I hope this helps you all. Many thanks Neil

Industry/Entity Type

Artists

Requirements
Must have
• Great menu system !

```html
<!DOCTYPE html>
<html lang="en">
<head>
<meta charset="utf-8">
<title>Velá Sorrin — Olive Oils, Vinegars &amp; Art</title>
<link href="https://fonts.googleapis.com/css2?family=Arimo:wght@400;700&family=PT+Sans:wght@400;700&display=swap" rel="stylesheet">
<style>
:root{
  --black:#070808;
  --green-deep:#0b3a1f;
  --green:#2f6b2e;
  --green-text:#3d6f25;
  --tab-top:#4c9a3f;
  --tab-bottom:#1f5d20;
  --nav-active:#f5e94a;
  --ink:#222;
  --muted:#555;
  --panel-line:#c9c9c9;
  --panel-head:#e6e6e6;
  --white:#fff;
  --oil:#d4b12a;
}
*{box-sizing:border-box;margin:0;padding:0}
html,body{width:726px;height:1200px;overflow:hidden;background:var(--white)}
body{position:relative;font-family:"Arimo",Arial,sans-serif;color:var(--ink)}
.abs{position:absolute}
a{color:inherit;text-decoration:none}

/* header */
.site-header{left:0;top:0;width:726px;height:148px;background:var(--black)}
.brand{left:48px;top:28px;width:110px;height:96px;display:flex;align-items:center;gap:6px}
.brand-dot{width:14px;height:14px;border-radius:50%;background:var(--green);flex:none}
.brand-name{font-family:"PT Sans",sans-serif;font-weight:400;font-size:17px;line-height:20px;color:var(--white)}
.account-links{left:462px;top:57px;font-size:9px;color:var(--white);word-spacing:1px}
.account-links span{margin:0 5px;color:#bbb}
.cart{left:632px;top:51px;display:flex;align-items:center;gap:4px;font-size:9px;color:var(--white)}

.main-nav{left:290px;top:122px;display:flex;gap:3px}
.nav-tab{width:80px;height:25px;border-radius:3px 3px 0 0;background:linear-gradient(var(--tab-top),var(--tab-bottom));
  color:var(--white);font-size:10.5px;display:flex;align-items:center;justify-content:center;letter-spacing:.2px}
.nav-tab.is-active{color:var(--nav-active)}
.dropdown{left:371px;top:148px;width:101px;height:82px;background:var(--green-deep);border-radius:0 0 4px 4px;z-index:3;padding-top:6px}
.dropdown a{display:block;font-size:10px;color:var(--white);padding:0 0 0 17px;height:23px;line-height:22px}
.dropdown a:first-child{background:#082a16}

/* hero */
.hero-band{left:0;top:148px;width:726px;height:278px;background:linear-gradient(#0e4a26,#0a3a1e 60%,#0b3f21)}
.hero-slide{left:34px;top:170px;width:658px;height:296px;box-shadow:0 6px 8px rgba(0,0,0,.25);
  background:radial-gradient(ellipse at 60% 70%,#c9a418 0%,#e8d27a 22%,#f3efe2 48%,#fbfaf6 75%)}
.hero-title{left:67px;top:234px;font-size:22px;color:var(--green);font-family:"Arimo",sans-serif}
.hero-copy{left:72px;top:283px;width:490px;font-size:13px;line-height:22px;color:#333}
.slider-dots{left:586px;top:438px;display:flex;gap:2px}
.slider-dots i{width:14px;height:14px;border-radius:50%;background:#111}
.slider-dots i:first-child{background:var(--green-deep)}

/* sidebar */
.side-box{left:16px;width:166px;border:1px solid var(--panel-line);background:var(--white)}
.side-head{position:absolute;left:-7px;width:180px;height:20px;background:linear-gradient(#fafafa,var(--panel-head));
  border:1px solid #bdbdbd;font-family:"PT Sans",sans-serif;font-size:11px;color:#1d2e1b;padding-left:16px;line-height:19px}
.newsletter-input{left:6px;top:43px;width:154px;height:18px;border:1px solid #ccc}
.subscribe{left:42px;top:70px;width:89px;height:19px;border:1px solid #aaa;border-radius:9px;background:linear-gradient(#fff,#dcdcdc);
  font-family:"PT Sans",sans-serif;font-size:11px;text-align:center;line-height:17px;color:#1d2e1b}
.club-head{font-size:17px;padding-left:24px;line-height:19px}
.club-copy{left:9px;top:33px;width:150px;font-size:8.5px;line-height:12px;color:#333}
.img-fill{position:absolute}
.buy-oil{left:76px;top:64px;width:84px;height:38px;background:linear-gradient(#f0f0f0,#cfcfcf);
  font-family:"PT Sans",sans-serif;font-size:12.5px;line-height:15px;color:#4f8a3a;padding:3px 0 0 14px}
.divider-dash{left:6px;top:124px;width:154px;border-top:1px dashed #999}
.buy-vinegar{left:90px;top:132px;font-family:"PT Sans",sans-serif;font-size:13px;line-height:17px;color:#1b1b1b}
.click-here{font-size:9px;font-weight:700;color:#111}

/* main */
.welcome{left:222px;top:496px;font-family:"PT Sans",sans-serif;font-size:18px;color:var(--green-text)}
.welcome b{font-weight:400;color:#111}
.body-copy{font-size:8px;line-height:15.5px;color:#333}
.section-title{font-family:"PT Sans",sans-serif;font-size:18px;color:var(--green-text)}
.sub-title{font-size:10px;color:var(--green-text)}
.dotted{left:225px;width:463px;border-top:1px dotted #777}
.vline{left:452px;top:710px;width:1px;height:166px;background:#ccc}

/* footer */
.site-footer{left:0;top:1118px;width:726px;height:82px;background:linear-gradient(#0d3d22,#0a2f1a)}
.card-badges{left:30px;top:1138px;display:flex;gap:3px}
.card-badges i{width:30px;height:19px;background:#d9d9d9;border:1px solid #fff}
.social{left:30px;top:1175px;display:flex;gap:4px}
.social i{width:22px;height:22px;border-radius:4px;background:#2d6bb0}
.social i:last-child{background:#e8812a}
.footer-links{left:258px;top:1147px;font-size:9px;color:var(--white)}
.footer-links span{margin:0 10px}
.copyright{left:287px;top:1169px;font-size:9px;color:var(--white)}
.contact{left:605px;top:1132px;font-size:8.5px;color:var(--white)}
.contact p{font-size:7.5px;line-height:10px;margin:7px 0 0 7px}
</style>
</head>
<body>

<header class="site-header abs" aria-label="Site header"></header>
<div class="brand abs"><span class="brand-dot"></span><span class="brand-name">Velá Sorrin</span></div>
<nav class="account-links abs"><a>Login</a><span>|</span><a>Create an account</a><span>|</span><a>My Cart</a></nav>
<div class="cart abs">
  <svg width="20" height="18" viewBox="0 0 20 18" aria-hidden="true"><path d="M1 2h3l2 9h10l2-7H5" fill="none" stroke="#ccc" stroke-width="1.6"/><circle cx="8" cy="15" r="1.6" fill="#ccc"/><circle cx="15" cy="15" r="1.6" fill="#ccc"/></svg>
  <span>(0) Items</span>
</div>

<nav class="main-nav abs">
  <a class="nav-tab is-active">HOME</a>
  <a class="nav-tab">OLIVE OILS</a>
  <a class="nav-tab">VINEGARS</a>
  <a class="nav-tab">ART</a>
  <a class="nav-tab">ABOUT US</a>
</nav>

<div class="hero-band abs"></div>
<div class="dropdown abs"><a>Region</a><a>flavor</a><a>Top Sellers</a></div>

<section class="hero-slide abs" role="img" aria-label="Glass bottles and decanters of golden olive oil with an olive sprig"></section>
<h1 class="hero-title abs" style="font-weight:400">Lorem ipsum dolor sit amet, adipiscing elit.</h1>
<p class="hero-copy abs">Lorem ipsum dolor sit amet, consectetuer adipiscing elit. Nam nibh. Nunc varius facilisis eros. Sed erat. Lorem ipsum dolor sit amet, consectetuer adipiscing elit. nibh. Nunc varius facilisis eros. Sed erat.</p>
<div class="slider-dots abs"><i></i><i></i><i></i><i></i><i></i></div>

<!-- sidebar -->
<aside>
  <div class="side-box abs" style="top:498px;height:106px">
    <div class="side-head" style="top:13px">NEWS LETTER</div>
    <div class="newsletter-input abs"></div>
    <div class="subscribe abs">SUBSCRIBE</div>
  </div>

  <div class="side-box abs" style="top:610px;height:73px">
    <div class="side-head club-head" style="top:9px">JOIN OUR CLUB</div>
    <p class="club-copy abs">Lorem Ipsum is simply dummy text of the printing and typesetting industry.</p>
  </div>

  <div class="side-box abs" style="top:690px;height:200px">
    <div class="side-head" style="top:11px">BUY NOW YOUR PRODUCTS</div>
    <div class="img-fill" role="img" aria-label="Two bottles of olive oil" style="left:32px;top:43px;width:42px;height:75px;background:linear-gradient(90deg,#2f4a12,#6a8a1c,#2f4a12)"></div>
    <div class="buy-oil abs">BUY NOW<br>OLIVE OIL</div>
    <div class="divider-dash abs"></div>
    <div class="img-fill" role="img" aria-label="Two bottles of balsamic vinegar" style="left:26px;top:135px;width:55px;height:53px;background:linear-gradient(90deg,#2a1a2a,#4b3040,#2a1a2a)"></div>
    <div class="buy-vinegar abs">BUY NOW<br>BALSAMIC<br>VINEGARS</div>
  </div>

  <div class="side-box abs" style="top:904px;height:206px">
    <div class="side-head" style="top:6px">BUY ART</div>
    <div class="img-fill" role="img" aria-label="Yellow sculpture of a figure opening its chest" style="left:1px;top:31px;width:164px;height:165px;background:radial-gradient(ellipse at 50% 45%,#e7b21a,#f0cf5a 45%,#fbf6e6 75%)"></div>
    <div class="click-here abs" style="left:13px;top:190px">CLICK HERE &nbsp;&gt;&gt;</div>
  </div>
</aside>

<!-- main content -->
<main>
  <h2 class="welcome abs" style="font-weight:400">Welcome to <b>Vela Sorrin</b></h2>
  <p class="body-copy abs" style="left:222px;top:534px;width:322px">Lorem ipsum dolor sit amet, consectetuer adipiscing elit. Nam nibh. Nunc varius facilisis eros. Sed erat. Lorem ipsum dolor sit amet, consectetuer adipiscing elit. nibh. Nunc varius facilisis eros. Sed erat. Lorem ipsum dolor sit amet, consectetuer adipiscing elit. Nam nibh. Nunc varius facilisis eros. Sed erat. Lorem ipsum dolor sit amet, consectetuer adipiscing elit.</p>
  <div class="img-fill" role="img" aria-label="Green and black olives on a sprig" style="left:555px;top:505px;width:145px;height:110px;background:radial-gradient(ellipse at 60% 50%,#7f8f1e,#a7b446 40%,#fff 72%)"></div>
  <p class="body-copy abs" style="left:222px;top:619px;width:478px">Lorem ipsum dolor sit amet, consectetuer adipiscing elit. Nam nibh. Nunc varius facilisis eros. Sed erat. Lorem ipsum dolor sit amet, consectetuer adipiscing elit. nibh. Nunc varius facilisis eros. Sed erat. Lorem ipsum dolor sit amet, consectetuer adipiscing elit. Nam nibh. Nunc varius facilisis eros. Sed erat. Lorem ipsum dolor sit amet, consectetuer adipiscing elit.</p>

  <div class="dotted abs" style="top:683px"></div>

  <h3 class="section-title abs" style="left:225px;top:702px;font-weight:400">Healthy Living</h3>
  <div class="img-fill" role="img" aria-label="Portrait photo of a man" style="left:232px;top:744px;width:56px;height:56px;background:linear-gradient(#e9e6e2,#b9a999)"></div>
  <p class="sub-title abs" style="left:296px;top:740px">Lorem ipsum dolor amet.</p>
  <p class="body-copy abs" style="left:296px;top:755px;width:120px;line-height:12px">Lorem ipsum dolor sit amet, consectetuer adipiscing elit. Nam nibh. Nunc varius facilisis eros. Sed erat.</p>
  <p class="body-copy abs" style="left:232px;top:812px;width:210px;line-height:12px">Lorem ipsum dolor sit amet, consectetuer adipiscing elit. Nam nibh. Nunc varius facilisis eros. Sed erat. Lorem ipsum dolor sit amet, consectetuer adipiscing elit.</p>

  <div class="vline abs"></div>

  <h3 class="section-title abs" style="left:473px;top:702px;font-weight:400">Featured Products</h3>
  <div class="img-fill" role="img" aria-label="Cruets of red vinegar and olive oil" style="left:482px;top:738px;width:56px;height:56px;background:linear-gradient(90deg,#9c2a2a,#f2efe8 50%,#c9a21c)"></div>
  <p class="sub-title abs" style="left:563px;top:734px">Lorem ipsum dolor amet.</p>
  <p class="body-copy abs" style="left:563px;top:754px;width:125px;line-height:12px">Lorem ipsum dolor sit amet, consectetuer adipiscing elit. Nam nibh. Nunc varius facilisis eros. Sed erat.</p>
  <div class="img-fill" role="img" aria-label="Three bottles of infused olive oil" style="left:484px;top:820px;width:56px;height:56px;background:linear-gradient(90deg,#b8901a,#e3c352,#b8901a)"></div>
  <p class="sub-title abs" style="left:565px;top:812px">Lorem ipsum dolor amet.</p>
  <p class="body-copy abs" style="left:565px;top:830px;width:125px;line-height:12px">Lorem ipsum dolor sit amet, consectetuer adipiscing elit. Nam nibh. Nunc varius facilisis eros. Sed erat.</p>

  <div class="dotted abs" style="top:893px"></div>

  <h3 class="section-title abs" style="left:224px;top:903px;font-weight:400">Healthy Recipes</h3>
  <div class="img-fill" role="img" aria-label="Grilled salmon fillet with fresh salad" style="left:222px;top:936px;width:182px;height:149px;border-radius:6px;border:1px solid #ccc;background:linear-gradient(135deg,#7faa3a,#d64a2a 35%,#b5602a 60%,#e8d9c0)"></div>
  <p class="sub-title abs" style="left:428px;top:929px">Lorem ipsum dolor amet.</p>
  <p class="body-copy abs" style="left:428px;top:949px;width:265px;line-height:12px">Lorem ipsum dolor sit amet, &nbsp;consectetuer adipiscing elit. Nam nibh. Nunc varius facilisis eros. Sed erat.</p>
  <p class="body-copy abs" style="left:428px;top:982px;width:265px;line-height:12px">Lorem ipsum dolor sit amet, consectetuer adipiscing elit. Nam nibh. Nunc varius facilisis eros. Sed erat.Lorem ipsum dolor sit amet, consectetuer adipiscing elit.</p>
  <p class="body-copy abs" style="left:428px;top:1023px;width:265px;line-height:12px">Lorem ipsum dolor sit amet, consectetuer adipiscing elit. Nam nibh. Nunc varius facilisis eros. Sed erat.Lorem ipsum dolor sit amet, consectetuer adipiscing elit.</p>
  <div class="click-here abs" style="left:607px;top:1072px">CLICK HERE &nbsp;&gt;&gt;</div>
</main>

<footer class="site-footer abs"></footer>
<div class="card-badges abs" aria-label="Accepted payment cards"><i></i><i></i><i></i><i></i></div>
<div class="social abs" aria-label="Social links"><i></i><i></i><i></i><i></i></div>
<nav class="footer-links abs"><a>Privacy Policy</a><span>|</span><a>Terms &amp; Conditions</a><span>|</span><a>Contact Us</a></nav>
<p class="copyright abs">© 2011 Velasorrin, All Rights Reserved</p>
<div class="contact abs">
  Contact Information
  <p>Lorem ipsum dolor sit<br>aconsectetuer adipiscing .<br>Email : info@velasorrin.com<br>Phone : &nbsp;555 014 2290</p>
</div>

</body>
</html>
```